Movie Poster/DVD jacket for Short Documentary

I am a documentary filmmaker who just completed a project titled "Sister Marigold". Here is the logline (short description of the movie): "An Oklahoma family is ripped apart after their 15-year-old son brutally murders his older sister in 1974. Controversy swirls around the case after his parents decide to hire a prominent defense attorney to keep him out of jail." I have several good photos of the family involved. I am in the process of submitting the film to several festivals and I want a professional looking movie poster that can be sent with film submissions. The look needs to dramatic and serious.
Updates

Project Deadline Extended Reason: We just had several more submission enter today and need a few more days to evaluate. Thank you for you patience. Added Thursday, November 19, 2015

Target Market(s)

Film festivals, television

Industry/Entity Type

Movie

Colors
f04a50

Requirements
Must have
• the color red and have a similar appearance to the sample movie posters.
• Also, tagline: turning a blind eye into broken hearts
• Directors name: a film by Rob Haskett
Nice to have
• rough
Should not have
• Not a gruesome look.

```html
<!DOCTYPE html>
<html lang="en">
<head>
<meta charset="utf-8">
<title>Sister Marigold — Festival Poster</title>
<link href="https://fonts.googleapis.com/css2?family=Big+Shoulders+Stencil+Display:wght@800;900&family=Oswald:wght@300;400&family=Montserrat:wght@400;800&display=swap" rel="stylesheet">
<style>
  :root {
    --backdrop: #bdbdbd;
    --poster-cream: #f1ecd2;
    --ink: #1c1a17;
    --title-silver: #e9e9e7;
    --title-shade: #7d7d7b;
    --accent-red: #f04a50;
    --seam-red: #b3262b;
    --band-red: #8e2a28;
    --photo-orange: #d5662f;
    --photo-rust: #a8402c;
    --photo-crimson: #8f2d33;
    --photo-teal: #5f8e94;
    --photo-sand: #e8ddb0;
    --photo-olive: #7d7a52;
    --lower-sage: #c3c396;
    --lower-cream: #e8e3c0;
  }
  * { box-sizing: border-box; margin: 0; padding: 0; }
  html, body { width: 1200px; height: 800px; overflow: hidden; }
  body { background: var(--backdrop); position: relative; }

  .poster {
    position: absolute; left: 332px; top: 20px;
    width: 535px; height: 760px;
    background: var(--poster-cream);
    overflow: hidden;
  }
  .poster__art {
    position: absolute; left: 12px; top: 14px; right: 12px; bottom: 14px;
    overflow: hidden;
  }
  .poster__photo {
    position: absolute; left: 0; top: 0; width: 100%; height: 520px;
    background:
      radial-gradient(ellipse 40% 30% at 10% 18%, var(--photo-teal) 0%, transparent 100%),
      radial-gradient(ellipse 45% 22% at 55% 12%, var(--photo-sand) 0%, transparent 100%),
      radial-gradient(ellipse 30% 25% at 92% 22%, #7f9aa0 0%, transparent 100%),
      radial-gradient(ellipse 35% 40% at 28% 58%, #c9775a 0%, transparent 100%),
      radial-gradient(ellipse 30% 38% at 62% 55%, var(--photo-orange) 0%, transparent 100%),
      radial-gradient(ellipse 30% 45% at 88% 55%, var(--photo-crimson) 0%, transparent 100%),
      radial-gradient(ellipse 35% 30% at 75% 92%, var(--photo-olive) 0%, transparent 100%),
      linear-gradient(180deg, #c2ae80 0%, var(--photo-rust) 55%, #8a4a34 100%);
  }
  .poster__seam {
    position: absolute; left: 0; top: 512px; width: 100%; height: 10px;
    background: var(--seam-red); opacity: .85;
  }
  .poster__lower {
    position: absolute; left: 0; top: 522px; width: 100%; bottom: 0;
    background:
      radial-gradient(ellipse 35% 40% at 18% 30%, #a9ab7c 0%, transparent 100%),
      radial-gradient(ellipse 30% 40% at 88% 45%, #a7a57a 0%, transparent 100%),
      linear-gradient(180deg, var(--lower-sage) 0%, var(--lower-cream) 65%, #d9d2ab 100%);
  }
  .tagline {
    position: absolute; top: 26px; left: 0; width: 100%;
    text-align: center;
    font-family: 'Oswald', sans-serif; font-weight: 400;
    font-size: 15px; letter-spacing: 4px; color: var(--ink);
  }
  .title {
    position: absolute; top: 352px; left: 0; width: 100%;
    text-align: center;
    font-family: 'Big Shoulders Stencil Display', sans-serif; font-weight: 900;
    font-size: 172px; line-height: 1; letter-spacing: 2px;
    color: var(--title-silver);
    text-shadow: 0 3px 0 var(--title-shade);
  }
  .subtitle {
    position: absolute; top: 500px; left: 0; width: 100%;
    text-align: center;
    font-family: 'Montserrat', sans-serif; font-weight: 800;
    font-size: 38px; line-height: 1; letter-spacing: 24px; padding-left: 24px;
    color: var(--accent-red);
  }
  .credit-lead {
    position: absolute; top: 604px; left: 0; width: 100%; text-align: center;
    font-family: 'Montserrat', sans-serif; font-weight: 400;
    font-size: 12px; color: var(--ink);
  }
  .director {
    position: absolute; top: 620px; left: 0; width: 100%; text-align: center;
    font-family: 'Montserrat', sans-serif; font-weight: 800;
    font-size: 20px; letter-spacing: 0.5px; color: #2a2824;
  }
  .rule { position: absolute; left: 40px; top: 666px; width: 431px; height: 4px; }
  .billing {
    position: absolute; left: 0; top: 704px; width: 100%; height: 26px;
    background: var(--band-red);
    display: flex; align-items: center; justify-content: center; gap: 6px;
    font-family: 'Oswald', sans-serif; font-weight: 300;
    font-size: 10px; letter-spacing: 0.5px; color: #f3d9c9; text-transform: uppercase;
  }
  .billing b { font-weight: 400; font-size: 12px; }
</style>
</head>
<body>
  <main class="poster">
    <div class="poster__art">
      <div class="poster__photo" role="img" aria-label="Weathered family snapshot of a young sister and brother, layered with rough orange, red and teal grunge textures"></div>
      <div class="poster__seam"></div>
      <div class="poster__lower" role="img" aria-label="Faded, cracked vintage photograph texture in pale sage tones"></div>

      <p class="tagline">TURNING A BLIND EYE INTO BROKEN HEARTS</p>
      <h1 class="title">SISTER</h1>
      <p class="subtitle">MARIGOLD</p>

      <p class="credit-lead">A FILM BY</p>
      <p class="director">ROB HASKETT</p>

      <svg class="rule" viewBox="0 0 431 4" preserveAspectRatio="none" aria-hidden="true">
        <line x1="0" y1="2" x2="431" y2="2" stroke="#fbf9ee" stroke-width="2.5"/>
      </svg>

      <p class="billing">
        <span>Produced by</span><b>Rob Haskett</b>
        <span>Directed by</span><b>Rob Haskett</b>
        <span>Produced by</span><b>Rob Haskett</b>
      </p>
    </div>
  </main>
</body>
</html>
```